Movie poster for short film: TINFOIL

We need a creative, artistic, stylized poster design for our short film TINFOIL. We would like to see designs with graphics and bold colors more than photographs. The photographs we are posting are more for reference- you do not have to use them in the poster! We are looking for something clean and simple. The film is a drama so please don't make it funny. The mood of the film is thoughtful and introspective. Name of film should be in all caps. Things to include in the poster:
Name of film: TINFOIL
Velvet Harbor Pictures
Starring Marisa Calloway

Here is a brief plot synopsis: TINFOIL follows one night in the life of a rebellious young woman who breaks into a diner after hours with a can of spray paint. Her intentions change after she ends up discovering what's left of a love story.

The movie is somewhat experimental, set to music for part of it with no dialog. The whole movie takes place in an old fashioned diner.

Target Market(s)

Film festival attendees between the ages of 20-50

Industry/Entity Type

Movie

Font styles to use
Sans Serif

Requirements
Must have
• See project description above- also the film is somewhat dark in nature so please don't make it too 'happy' looking.

```html
<!DOCTYPE html>
<html lang="en">
<head>
<meta charset="utf-8">
<title>TINFOIL – Poster</title>
<link rel="stylesheet" href="https://fonts.googleapis.com/css2?family=Anton&family=Questrial&display=swap">
<style>
  :root {
    --bg-deep: #1b0626;
    --bg-mid: #340a4a;
    --bg-glow: #5b1284;
    --ghost-text: rgba(255, 255, 255, 0.10);
    --ink: #ffffff;
    --dot: rgba(36, 14, 50, 0.75);
    --emblem-a: #2f5fd0;
    --emblem-b: #3a98a2;
    --emblem-c: #b39a4a;
  }
  * { margin: 0; padding: 0; box-sizing: border-box; }
  html, body { width: 1200px; height: 1000px; overflow: hidden; background: var(--bg-deep); }
  .poster {
    position: relative; width: 1200px; height: 1000px; overflow: hidden;
    background:
      radial-gradient(ellipse 900px 700px at 1000px 180px, var(--bg-glow) 0%, var(--bg-mid) 45%, transparent 100%),
      linear-gradient(90deg, var(--bg-deep) 0%, var(--bg-mid) 60%, var(--bg-mid) 100%);
  }
  .ghost-word {
    position: absolute; font-family: "Anton", sans-serif; font-size: 150px; line-height: 1;
    letter-spacing: 30px; color: var(--ghost-text); white-space: nowrap;
    transform: scaleX(1.25); transform-origin: left top;
  }
  .ghost-word--top { left: 600px; top: -30px; }
  .ghost-word--bottom { left: 600px; top: 884px; }
  .ghost-word--left { left: -8px; top: 20px; }
  .dot { position: absolute; border-radius: 50%; background: var(--dot); }
  .emblem-area {
    position: absolute; left: 140px; top: 268px; width: 210px; height: 225px; border-radius: 12px;
    background: linear-gradient(160deg, var(--emblem-a) 0%, var(--emblem-b) 50%, var(--emblem-c) 100%);
    opacity: 0.85;
  }
  .presenter {
    position: absolute; left: 357px; top: 297px; font-family: "Questrial", sans-serif;
    font-size: 35px; color: var(--ink); white-space: nowrap;
  }
  .title {
    position: absolute; left: 231px; top: 344px; font-family: "Anton", sans-serif;
    font-size: 160px; line-height: 1; color: var(--ink); letter-spacing: 2px;
    transform: scaleX(1.3); transform-origin: left top; white-space: nowrap;
  }
  .billing {
    position: absolute; left: 244px; top: 512px; font-family: "Questrial", sans-serif;
    font-size: 35px; color: var(--ink); white-space: nowrap;
  }
</style>
</head>
<body>
<main class="poster">
  <div class="ghost-word ghost-word--top" aria-hidden="true">TINFO</div>
  <div class="ghost-word ghost-word--bottom" aria-hidden="true">TINFO</div>
  <div class="ghost-word ghost-word--left" aria-hidden="true">IL</div>

  <span class="dot" style="left:313px;top:-35px;width:120px;height:120px"></span>
  <span class="dot" style="left:1078px;top:282px;width:66px;height:66px"></span>
  <span class="dot" style="left:853px;top:453px;width:60px;height:60px"></span>
  <span class="dot" style="left:412px;top:703px;width:120px;height:120px"></span>
  <span class="dot" style="left:970px;top:740px;width:120px;height:120px"></span>
  <span class="dot" style="left:57px;top:880px;width:120px;height:120px"></span>

  <div class="emblem-area" role="img" aria-label="Space for the film's key graphic"></div>

  <p class="presenter">Velvet Harbor Pictures Presents</p>
  <h1 class="title">TINFOIL</h1>
  <p class="billing">Starring: Marisa Calloway</p>
</main>
</body>
</html>
```